electrical contractor business card for professional modern company

I need a business card design for an electrical contractors business. I do all kinds of electricical work from new homes, air conditioning, data and communications. I have a logo design i want on it and have a good idea in my head of what i want it to look like. I like simple yet bold and professional looking. All black background is a must

Target Market(s)

Anyone needing electrical work done

Industry/Entity Type

Electrical

Contact Information for Business Card

company name- KTW Electrical and Data
person name-martin pellowe
phone number- 0418 362 927
website-ktwelec.example.com.au

Font styles to use
Sans Serif

Requirements
Must have
• email
• website
• logo
• name
• phone number
• list of work i do:
• -electrical
• -air-conditioning
• -data/communications
• -cctv/security
• -domestic/commercial/industrial
• -24hr emergency breakdown repair
Nice to have
• i would like the logo on the front side in the centre taking up most of the card with black background.
• on the rear i want the list of work i do with company info i.e. email, website, my name, phone number. rear of card also black background with orange writing to match the orange in the logo

```html
<!DOCTYPE html>
<html lang="en">
<head>
<meta charset="utf-8">
<title>KTW Electrical and Data – Business Card</title>
<link rel="stylesheet" href="https://fonts.googleapis.com/css2?family=Exo+2:wght@400;500&family=Open+Sans:wght@400&display=swap">
<style>
  :root {
    --backdrop: #8a6a48;
    --card: #000000;
    --card-back: #05070d;
    --orange: #f26b21;
    --amber: #f5a623;
    --spark-core: #dfe9ff;
    --spark-glow: #3a6fd0;
    --wire-copper: #b06a3a;
  }
  html, body {
    margin: 0;
    width: 900px;
    height: 1200px;
    overflow: hidden;
    background: var(--backdrop);
  }
  .canvas {
    position: relative;
    width: 900px;
    height: 1200px;
  }
  .card {
    position: absolute;
    left: 45px;
    width: 812px;
    background: var(--card);
    box-shadow: 0 4px 10px rgba(0,0,0,0.45);
    overflow: hidden;
  }
  .card--front { top: 80px; height: 500px; }
  .card--back { top: 618px; height: 502px; background: var(--card-back); }

  .rule {
    position: absolute;
    height: 4px;
    background: var(--orange);
  }
  .rule--top { top: 48px; left: 0; width: 700px; }
  .rule--bottom { top: 462px; left: 0; width: 812px; }

  .power-icon {
    position: absolute;
    top: 24px;
    left: 724px;
    width: 62px;
    height: 62px;
  }

  .brand {
    position: absolute;
    font-family: "Exo 2", sans-serif;
    font-weight: 500;
    color: var(--orange);
    white-space: nowrap;
    display: flex;
    align-items: center;
  }
  .brand__dot {
    border-radius: 50%;
    background: var(--orange);
    flex: none;
  }
  .brand--front {
    top: 230px;
    left: 0;
    width: 812px;
    justify-content: center;
    font-size: 34px;
    letter-spacing: 1px;
    gap: 16px;
  }
  .brand--front .brand__dot { width: 22px; height: 22px; }
  .brand--back {
    right: 32px;
    bottom: 36px;
    font-size: 20px;
    letter-spacing: 0.5px;
    gap: 10px;
  }
  .brand--back .brand__dot { width: 14px; height: 14px; }

  .spark-photo {
    position: absolute;
    left: 0;
    top: 0;
    width: 620px;
    height: 400px;
    background:
      radial-gradient(ellipse 150px 90px at 300px 170px, rgba(223,233,255,0.75), rgba(58,111,208,0.35) 55%, transparent 100%),
      radial-gradient(ellipse 340px 220px at 290px 190px, rgba(58,111,208,0.35), transparent 75%),
      linear-gradient(160deg, rgba(176,106,58,0.25) 0%, transparent 30%);
  }

  .contact {
    position: absolute;
    top: 28px;
    right: 32px;
    text-align: right;
    color: var(--amber);
    font-family: "Open Sans", sans-serif;
  }
  .contact__name {
    font-size: 36px;
    line-height: 46px;
    margin: 0 0 10px;
    font-weight: 400;
    letter-spacing: 0.5px;
  }
  .contact__line {
    font-size: 22px;
    line-height: 30px;
    color: var(--orange);
    display: flex;
    justify-content: flex-end;
    align-items: center;
    gap: 8px;
  }
  .contact__icon { width: 18px; height: 18px; }

  .services {
    position: absolute;
    left: 32px;
    top: 300px;
    margin: 0;
    padding: 0;
    list-style: none;
    font-family: "Exo 2", sans-serif;
    font-size: 22px;
    line-height: 30.5px;
    color: var(--orange);
    letter-spacing: 0.6px;
  }
  .services li {
    display: flex;
    align-items: center;
    gap: 12px;
  }
  .services li::before {
    content: "";
    width: 11px;
    height: 11px;
    border: 3px solid var(--orange);
    border-radius: 50%;
    flex: none;
  }
</style>
</head>
<body>
<main class="canvas">
  <section class="card card--front">
    <div class="rule rule--top"></div>
    <svg class="power-icon" viewBox="0 0 62 62" aria-hidden="true">
      <path d="M19 16 A22 22 0 1 0 43 16" fill="none" stroke="var(--orange)" stroke-width="5.5" stroke-linecap="round"/>
      <line x1="31" y1="7" x2="31" y2="30" stroke="var(--orange)" stroke-width="5.5" stroke-linecap="round"/>
    </svg>
    <div class="brand brand--front">
      <span class="brand__dot"></span>
      <span>KTW Electrical and Data</span>
    </div>
    <div class="rule rule--bottom"></div>
  </section>

  <section class="card card--back">
    <div class="spark-photo" role="img" aria-label="Photo of two stripped electrical wires with a bright blue electric spark arcing between them"></div>

    <div class="contact">
      <p class="contact__name">Martin pellowe</p>
      <div class="contact__line">
        <span>0418 362 927</span>
        <svg class="contact__icon" viewBox="0 0 18 18" aria-hidden="true">
          <circle cx="9" cy="9" r="7.5" fill="none" stroke="var(--orange)" stroke-width="1.8"/>
          <path d="M6 5.2 L7.4 5 L8.1 7 L7.2 7.7 Q8 9.6 10.2 10.8 L10.9 9.9 L12.9 10.6 L12.7 12 Q11.8 12.9 10 12.2 Q6.4 10.6 5.4 7 Q5.2 5.8 6 5.2 Z" fill="var(--orange)"/>
        </svg>
      </div>
      <div class="contact__line">
        <span>www.ktwelec.example.com.au</span>
        <svg class="contact__icon" viewBox="0 0 18 18" aria-hidden="true">
          <rect x="1" y="1" width="16" height="16" rx="4" fill="var(--orange)"/>
          <circle cx="9" cy="9" r="4.8" fill="none" stroke="var(--card-back)" stroke-width="1.4"/>
          <line x1="4.2" y1="9" x2="13.8" y2="9" stroke="var(--card-back)" stroke-width="1.2"/>
          <ellipse cx="9" cy="9" rx="2" ry="4.8" fill="none" stroke="var(--card-back)" stroke-width="1.2"/>
        </svg>
      </div>
    </div>

    <ul class="services">
      <li>Electrical</li>
      <li>Air-conditioning</li>
      <li>Data/communications</li>
      <li>Cctv/security</li>
      <li>Domestic/commercial/industrial</li>
      <li>24hr emergency breakdown repair</li>
    </ul>

    <div class="brand brand--back">
      <span class="brand__dot"></span>
      <span>KTW Electrical and Data</span>
    </div>
  </section>
</main>
</body>
</html>
```